Book cover for a book about how to support a friend in grief.

The title of the book is "Quiet Hands on Heavy Days: Standing Beside Someone Across Hard Seasons" by Daniel P. Hartwig. I am a grief counselor and am passionate about educating people on how to better support someone in grief. I'd like the cover to tell a story. Maybe a person in grief and a friend standing near who doesn't know what to say. The image should appeal to all genders. I am open to ANY other ideas for the cover. Grief is a heavy topic but I don't want the cover to feel sad. It should convey hope.

```html
<!DOCTYPE html>
<html lang="en">
<head>
<meta charset="utf-8">
<title>Quiet Hands on Heavy Days — Book Cover</title>
<link rel="stylesheet" href="https://fonts.googleapis.com/css2?family=Cinzel:wght@400;500;700&family=Cormorant+Garamond:ital,wght@1,500&display=swap">
<style>
  :root {
    --page: #ffffff;
    --sky-top: #414a5b;
    --sky-mid: #8b8176;
    --sky-warm: #c9a47a;
    --sky-glow: #f2ac5e;
    --sky-low: #e48f3c;
    --ground: #000000;
    --title-white: #ffffff;
    --title-yellow: #fff200;
  }
  * { margin: 0; padding: 0; box-sizing: border-box; }
  html, body {
    width: 1200px;
    height: 1200px;
    overflow: hidden;
    background: var(--page);
  }
  .cover {
    position: absolute;
    left: 247px;
    top: 71px;
    width: 703px;
    height: 1055px;
    overflow: hidden;
    background: var(--ground);
  }
  .cover__sky {
    position: absolute;
    left: 0;
    top: 0;
    width: 100%;
    height: 873px;
    background:
      radial-gradient(ellipse 70% 40% at 10% 95%, rgba(255, 210, 140, 0.55), rgba(255, 210, 140, 0) 70%),
      linear-gradient(180deg,
        var(--sky-top) 0%,
        var(--sky-mid) 35%,
        var(--sky-warm) 60%,
        var(--sky-glow) 82%,
        var(--sky-low) 100%);
  }
  .cover__ground {
    position: absolute;
    left: 0;
    top: 873px;
    width: 100%;
    height: 182px;
    background: var(--ground);
  }
  .cover__text {
    position: absolute;
    left: 0;
    width: 100%;
    text-align: center;
    white-space: nowrap;
    line-height: 1;
  }
  .title-lead {
    font-family: "Cinzel", serif;
    font-weight: 400;
    font-size: 41px;
    color: var(--title-white);
    letter-spacing: 1px;
    top: 100px;
  }
  .title-main {
    font-family: "Cinzel", serif;
    font-weight: 700;
    font-size: 156px;
    color: var(--title-yellow);
    letter-spacing: 2px;
  }
  .title-main--one { top: 146px; }
  .title-main--two { top: 273px; }
  .subtitle {
    font-family: "Cormorant Garamond", serif;
    font-style: italic;
    font-weight: 500;
    font-size: 40px;
    line-height: 50px;
    color: var(--title-white);
    top: 482px;
    left: -8px;
  }
  .author {
    font-family: "Cinzel", serif;
    font-weight: 400;
    font-size: 52px;
    color: var(--title-white);
    letter-spacing: 1px;
    top: 944px;
  }
</style>
</head>
<body>
  <div class="cover">
    <div class="cover__sky" role="img" aria-label="Sunset sky photograph with silhouettes of a grieving person seated on a bench and a friend standing nearby, head bowed"></div>
    <div class="cover__ground"></div>
    <h1>
      <span class="cover__text title-lead">QUIET HANDS ON</span>
      <span class="cover__text title-main title-main--one">HEAVY</span>
      <span class="cover__text title-main title-main--two">DAYS</span>
    </h1>
    <p class="cover__text subtitle">Standing Beside Someone<br>Across Hard Seasons</p>
    <p class="cover__text author">DANIEL P. HARTWIG</p>
  </div>
</body>
</html>
```